Training Consultant for Oil and Gas Drillers needs logo for business cards

I teach oil and gas professionals the skills required to keep rigs from blowing up. The company name is "Night Shift Bore Safety", which is pronounced Nite Shiffed. Tour refers to the time on an oil rig when a worker is off for sleep and rest. I teach something called Well Control, which is how to maintain a pressure balance in the well so the hydro carbons don't come to surface unexpectedly( like the Grey Tide Platform).

Target Market(s)

Rig hands and oil companies

Contact Information for Business Card

Night Shift BS ( company name) with a new logo
My name (Derek Holloway )and Title (Well Control Consultant)
Phone number and address

Font styles to use
Serif
Sans Serif

Colors

Designer to choose colors to be used in the design.

Requirements
Must have
• I need a logo for the company. I do not have anything yet

```html
<!DOCTYPE html>
<html lang="en">
<head>
<meta charset="utf-8">
<title>Night Shift Bore Safety – Business Card</title>
<link rel="stylesheet" href="https://fonts.googleapis.com/css2?family=Lato:wght@400;900&family=Oswald:wght@600&display=swap">
<style>
  :root {
    --page-bg: #eef1f4;
    --card-white: #ffffff;
    --brand-blue: #3d8fd1;
    --back-blue: #62a9dc;
    --title-blue: #2f6fbf;
    --ink: #2a2a2a;
    --ink-soft: #3a3a3a;
  }
  * { margin: 0; padding: 0; box-sizing: border-box; }
  html, body {
    width: 1200px; height: 1200px; overflow: hidden;
    background: var(--page-bg);
  }
  .canvas {
    width: 1200px; height: 1200px;
    display: flex; flex-direction: column;
    align-items: center; justify-content: center; gap: 60px;
  }
  .card {
    width: 840px; height: 480px;
    position: relative;
    box-shadow: 0 6px 18px rgba(0,0,0,0.12);
  }
  .card--back {
    background: var(--back-blue);
    display: flex; align-items: center; justify-content: center;
  }
  .card--front { background: var(--card-white); }

  .brand { display: flex; align-items: center; gap: 22px; }
  .brand__dot { width: 74px; height: 74px; border-radius: 50%; flex: none; }
  .brand__name {
    font-family: "Lato", sans-serif; font-weight: 900;
    text-transform: uppercase; line-height: 1.05; letter-spacing: 1px;
  }
  .card--back .brand__dot { background: var(--card-white); width: 110px; height: 110px; }
  .card--back .brand__name { color: var(--card-white); font-size: 52px; }

  .card--front .brand {
    position: absolute; left: 60px; top: 170px;
  }
  .card--front .brand__dot { background: var(--brand-blue); }
  .card--front .brand__name { color: var(--brand-blue); font-size: 32px; }

  .divider {
    position: absolute; left: 468px; top: 150px;
    width: 3px; height: 180px; background: var(--brand-blue);
  }
  .contact {
    position: absolute; left: 500px; top: 148px;
    font-family: "Lato", sans-serif; color: var(--ink-soft);
  }
  .contact__name {
    font-family: "Oswald", sans-serif; font-weight: 600;
    font-size: 38px; color: var(--ink); text-transform: uppercase;
    line-height: 1.05;
  }
  .contact__title { font-size: 20px; color: var(--title-blue); margin-bottom: 8px; }
  .contact__address { font-size: 19px; line-height: 1.2; margin-bottom: 20px; }
  .contact__list { list-style: none; font-size: 18px; line-height: 1.35; }
  .contact__list li { display: flex; align-items: center; gap: 8px; }
  .contact__icon { width: 13px; height: 13px; fill: var(--brand-blue); flex: none; }
</style>
</head>
<body>
<main class="canvas">
  <section class="card card--back" aria-label="Card back">
    <div class="brand">
      <span class="brand__dot"></span>
      <span class="brand__name">Night Shift<br>Bore Safety</span>
    </div>
  </section>

  <section class="card card--front" aria-label="Card front">
    <div class="brand">
      <span class="brand__dot"></span>
      <span class="brand__name">Night Shift<br>Bore Safety</span>
    </div>
    <div class="divider"></div>
    <div class="contact">
      <h1 class="contact__name">Derek Holloway</h1>
      <p class="contact__title">Well Control Consultant</p>
      <p class="contact__address">Linden Quay Terrace, Harbour Road<br>Portvale C4410, Brazil</p>
      <ul class="contact__list">
        <li>
          <svg class="contact__icon" viewBox="0 0 24 24" aria-hidden="true"><path d="M6.6 10.8a15.1 15.1 0 0 0 6.6 6.6l2.2-2.2a1 1 0 0 1 1-.25 11.4 11.4 0 0 0 3.6.57 1 1 0 0 1 1 1V20a1 1 0 0 1-1 1A17 17 0 0 1 3 4a1 1 0 0 1 1-1h3.5a1 1 0 0 1 1 1c0 1.25.2 2.45.57 3.57a1 1 0 0 1-.25 1z"/></svg>
          4410 -527- 0983
        </li>
        <li>
          <svg class="contact__icon" viewBox="0 0 24 24" aria-hidden="true"><path d="M2 5h20v14H2z M2 5l10 8 10-8" /></svg>
          hello@nightshiftbs.example
        </li>
        <li>
          <svg class="contact__icon" viewBox="0 0 24 24" aria-hidden="true"><circle cx="12" cy="12" r="10"/></svg>
          www.nightshiftbs.example
        </li>
      </ul>
    </div>
  </section>
</main>
</body>
</html>
```